Android Payment Application UI Design

We require a UI/UX design for an existing Android card-based payment application.

We're looking to improve the look + feel of the existing app. What we're after:
- Colour palette options
- Fonts
- Icons

See attached document for existing screen types, icons, etc.

All resources provided must be royalty free.

It's to run on a specialised device, with 720 x 1280 pixel resolution, in portrait only (landscape not required).

Please provide mockup examples of the new screen layout applied to the existing screens in the document.

Target Market(s)

Retail business users

Font styles to use
Sans Serif

Colors

Designer to choose colors to be used in the design.

Requirements
Must have
• Looking for
• - modern design
• - simple colours, easy-to-read sans-serif fonts
• - cohesive, consistent design between screens

```html
<!DOCTYPE html>
<html lang="en">
<head>
<meta charset="utf-8">
<title>TilloPay – Android Payment App Screens</title>
<link href="https://fonts.googleapis.com/css2?family=Roboto:wght@300;400;500;700&display=swap" rel="stylesheet">
<style>
:root{
  --sky:#4bbde0;
  --navy:#1d2a5c;
  --brand:#1a8fd0;
  --ink:#22262b;
  --muted:#8a9097;
  --line:#e3e6ea;
  --orange:#ff6a13;
  --option-a:#2f3f7a;
  --option-b:#3b86b0;
  --bg:#ffffff;
}
*{box-sizing:border-box;margin:0;padding:0}
html,body{width:1200px;height:1200px;overflow:hidden;background:var(--bg);font-family:'Roboto',sans-serif;color:var(--ink)}
.board{position:relative;width:1200px;height:1200px}
.screen{position:absolute;width:261px;height:490px;background:#fff;border-radius:22px;box-shadow:0 8px 26px rgba(30,40,60,.10);overflow:hidden}
.screen.blue{background:var(--sky)}
.brand{position:absolute;left:0;right:0;display:flex;align-items:center;justify-content:center;gap:5px;font-weight:700;color:var(--navy);letter-spacing:.5px}
.brand .dot{border-radius:50%;background:var(--brand)}
.brand.sm{font-size:15px}.brand.sm .dot{width:14px;height:14px}
.brand.lg{font-size:42px;gap:10px}.brand.lg .dot{width:40px;height:40px}
.footer{position:absolute;left:0;right:0;text-align:center;font-size:8px;font-weight:500}
.footer .ver{font-size:5.5px;color:var(--muted);font-weight:400;margin-left:3px}
.footer small{display:block;font-size:5.5px;margin-top:4px}
.welcome{position:absolute;top:118px;left:0;right:0;text-align:center;font-size:35px;font-weight:300;color:#3a4048}
.login-box{position:absolute;left:38px;top:208px;width:183px;height:102px;border:1px solid var(--line);border-radius:5px}
.login-box .field{height:51px;display:flex;align-items:center;justify-content:center;font-size:8px;color:var(--muted);position:relative}
.login-box .field+.field{border-top:1px solid var(--line)}
.login-box .eye{position:absolute;right:14px;top:20px}
.forgot{position:absolute;top:333px;left:0;right:0;text-align:center;font-size:6px;font-weight:500}
.btn-login{position:absolute;left:38px;top:366px;width:183px;height:34px;border-radius:17px;background:var(--sky);color:#fff;font-size:8px;font-weight:700;display:flex;align-items:center;justify-content:center}
.header{position:absolute;left:0;top:0;width:100%;height:142px;background:var(--sky)}
.battery{position:absolute;top:32px;right:19px;width:66px;height:14px;border-radius:7px;background:var(--orange);color:#fff;font-size:6px;font-weight:500;display:flex;align-items:center;justify-content:center;gap:5px}
.kebab{position:absolute;width:3px}
.kebab i{display:block;width:3px;height:3px;border-radius:50%;background:currentColor;margin-bottom:2px}
.tabs{position:absolute;top:120px;left:0;right:0;height:22px;display:flex;justify-content:space-between;padding:0 21px;color:#fff;font-size:11px}
.tabs .active{font-weight:500;position:relative}
.tabs .active::after{content:"";position:absolute;left:-21px;bottom:-5px;width:130px;height:2px;background:rgba(255,255,255,.55)}
.menu{position:absolute;top:152px;left:0;right:0;list-style:none}
.menu li{height:45px;display:flex;align-items:center;position:relative;font-size:11.5px}
.menu li svg{position:absolute;left:14px;top:14px}
.menu li span{position:absolute;left:52px}
.menu li+li::before{content:"";position:absolute;left:52px;right:12px;top:0;height:1px;background:var(--line)}
.dropdown{position:absolute;left:134px;top:98px;width:107px;height:166px;background:#fff;box-shadow:0 4px 14px rgba(0,0,0,.14);border-radius:2px;padding:1px 0;z-index:2}
.dropdown div{height:26.5px;display:flex;align-items:center;font-size:6.5px;color:#555;padding-left:29px;position:relative}
.dropdown div+div{border-top:1px solid #eef0f2}
.dropdown div i{position:absolute;left:10px;top:10px;width:7px;height:6px;border:1px solid #8a9097;border-radius:1px}
.back{position:absolute;left:18px}
.title{position:absolute;left:18px;top:122px;font-size:22px;font-weight:300}
.hint{position:absolute;left:18px;top:152px;font-size:8.5px;font-weight:500}
.amount-box{position:absolute;left:29px;top:246px;width:205px;height:34px;border:1px solid var(--line);border-radius:4px;display:flex;align-items:center;justify-content:space-between;padding:0 9px 0 13px;font-size:17px}
.amount-box small,.amount small{font-size:7.5px;color:var(--muted)}
.amount{position:absolute;right:19px;top:126px;font-size:17px}
.pay-option{position:absolute;top:216px;width:58px;height:58px;border-radius:50%}
.opt-a{left:16px;background:var(--option-a)}
.opt-b{left:101px;background:var(--option-b)}
.opt-c{left:185px;border:1px solid var(--sky);background:#fff}
.tap{position:absolute;top:345px;left:0;right:0;text-align:center;font-size:18px;font-weight:300;color:#3a4048}
.tap small{display:block;font-size:8.5px;font-weight:500;color:var(--ink)}
.terminal-art{position:absolute;left:102px;top:172px;width:76px;height:84px;border-radius:6px;background:linear-gradient(135deg,#1e4fc4,#10318c)}
.swiping{position:absolute;top:392px;left:0;right:0;text-align:center;color:#fff;font-size:11px;font-weight:300}
</style>
</head>
<body>
<div class="board">

  <section class="screen" style="left:22px;top:52px">
    <div class="brand lg" style="top:183px"><span class="dot"></span>Tillora</div>
    <div class="footer" style="top:441px">TilloPay<span class="ver">(0.0.1)</span><small>(Tillora UK Demo)</small></div>
  </section>

  <section class="screen" style="left:325px;top:52px">
    <div class="brand sm" style="top:48px"><span class="dot"></span>Tillora</div>
    <h1 class="welcome">Welcome</h1>
    <div class="login-box">
      <div class="field">Email address / User ID</div>
      <div class="field">Password
        <svg class="eye" width="10" height="8" viewBox="0 0 10 8"><path d="M1 4 Q5 0 9 4 Q5 8 1 4Z" fill="none" stroke="#8a9097"/><line x1="1" y1="7" x2="9" y2="1" stroke="#8a9097"/></svg>
      </div>
    </div>
    <div class="forgot">Forgot Password?</div>
    <div class="btn-login">LOGIN</div>
    <div class="footer" style="top:441px">TilloPay<span class="ver">(0.0.1)</span><small>(Tillora UK Demo)</small></div>
  </section>

  <section class="screen" style="left:622px;top:52px">
    <header class="header">
      <div class="battery">Low Battery <svg width="8" height="9" viewBox="0 0 8 9"><rect x="1" y="1" width="4" height="7" rx="1" fill="none" stroke="#fff"/><line x1="6" y1="5" x2="8" y2="5" stroke="#fff"/></svg></div>
      <div class="brand sm" style="top:72px"><span class="dot"></span>Tillora</div>
      <div class="kebab" style="right:21px;top:77px;color:#fff"><i></i><i></i><i></i></div>
      <nav class="tabs"><span class="active">Main menu</span><span>Admin menu</span></nav>
    </header>
    <ul class="menu">
      <li><svg width="16" height="16" viewBox="0 0 16 16" fill="none" stroke="#9aa0a6" stroke-width="1.4"><path d="M1 15H15M3 14V6M6 14V3M9 14V8M12 14V10"/></svg><span style="font-weight:500">Sales</span></li>
      <li><svg width="16" height="16" viewBox="0 0 16 16" fill="none" stroke="#9aa0a6" stroke-width="1.4"><path d="M2 7V5H13L11 3M14 9V11H3L5 13"/></svg><span>Reversal</span></li>
      <li><svg width="16" height="16" viewBox="0 0 16 16" fill="none" stroke="#9aa0a6" stroke-width="1.4"><path d="M4 5A5 5 0 1 1 3 9M4 2V5H7"/></svg><span>Refund</span></li>
      <li><svg width="16" height="16" viewBox="0 0 16 16" fill="none" stroke="#9aa0a6" stroke-width="1.4"><circle cx="8" cy="6" r="4"/><path d="M5 9L4 15L8 13L12 15L11 9"/></svg><span>Pre-Auth</span></li>
      <li><svg width="16" height="16" viewBox="0 0 16 16" fill="none" stroke="#9aa0a6" stroke-width="1.4"><circle cx="8" cy="8" r="6.5"/><path d="M5 8L7 10L11 6"/></svg><span>Completion</span></li>
      <li><svg width="16" height="16" viewBox="0 0 16 16" fill="none" stroke="#9aa0a6" stroke-width="1.4"><path d="M4 6H14L12 4M12 10H2L4 12"/></svg><span>Reconciliation</span></li>
      <li><svg width="16" height="16" viewBox="0 0 16 16" fill="none" stroke="#9aa0a6" stroke-width="1.4"><rect x="4" y="2" width="8" height="4"/><rect x="1.5" y="6" width="13" height="6" rx="1"/><rect x="4" y="10" width="8" height="4"/></svg><span>Reprint Manager</span></li>
    </ul>
  </section>

  <section class="screen" style="left:918px;top:52px">
    <header class="header">
      <div class="battery">Low Battery <svg width="8" height="9" viewBox="0 0 8 9"><rect x="1" y="1" width="4" height="7" rx="1" fill="none" stroke="#fff"/><line x1="6" y1="5" x2="8" y2="5" stroke="#fff"/></svg></div>
      <div class="brand sm" style="top:72px"><span class="dot"></span>Tillora</div>
      <div class="kebab" style="right:21px;top:77px;color:#fff"><i></i><i></i><i></i></div>
      <nav class="tabs"><span class="active">Main menu</span><span></span></nav>
    </header>
    <div class="dropdown">
      <div><i></i>Logout</div>
      <div><i></i>Settings</div>
      <div><i></i>Wifi Settings</div>
      <div><i></i>Data Settings</div>
      <div><i></i>Input Settings</div>
      <div><i></i>App Settings</div>
    </div>
    <ul class="menu">
      <li><svg width="16" height="16" viewBox="0 0 16 16" fill="none" stroke="#9aa0a6" stroke-width="1.4"><path d="M1 15H15M3 14V6M6 14V3M9 14V8M12 14V10"/></svg><span style="font-weight:500">Sales</span></li>
      <li><svg width="16" height="16" viewBox="0 0 16 16" fill="none" stroke="#9aa0a6" stroke-width="1.4"><path d="M2 7V5H13L11 3M14 9V11H3L5 13"/></svg><span>Reversal</span></li>
      <li><svg width="16" height="16" viewBox="0 0 16 16" fill="none" stroke="#9aa0a6" stroke-width="1.4"><path d="M4 5A5 5 0 1 1 3 9M4 2V5H7"/></svg><span>Refund</span></li>
      <li><svg width="16" height="16" viewBox="0 0 16 16" fill="none" stroke="#9aa0a6" stroke-width="1.4"><circle cx="8" cy="6" r="4"/><path d="M5 9L4 15L8 13L12 15L11 9"/></svg><span>Pre-Auth</span></li>
      <li><svg width="16" height="16" viewBox="0 0 16 16" fill="none" stroke="#9aa0a6" stroke-width="1.4"><circle cx="8" cy="8" r="6.5"/><path d="M5 8L7 10L11 6"/></svg><span>Completion</span></li>
      <li><svg width="16" height="16" viewBox="0 0 16 16" fill="none" stroke="#9aa0a6" stroke-width="1.4"><path d="M4 6H14L12 4M12 10H2L4 12"/></svg><span>Reconciliation</span></li>
      <li><svg width="16" height="16" viewBox="0 0 16 16" fill="none" stroke="#9aa0a6" stroke-width="1.4"><rect x="4" y="2" width="8" height="4"/><rect x="1.5" y="6" width="13" height="6" rx="1"/><rect x="4" y="10" width="8" height="4"/></svg><span>Reprint Manager</span></li>
    </ul>
  </section>

  <section class="screen" style="left:21px;top:667px">
    <svg class="back" style="top:64px" width="16" height="10" viewBox="0 0 16 10" fill="none" stroke="#555" stroke-width="1.4"><path d="M15 5H2M6 1L2 5L6 9"/></svg>
    <div class="brand sm" style="top:60px"><span class="dot"></span>Tillora</div>
    <div class="kebab" style="right:20px;top:62px;color:#777"><i></i><i></i><i></i></div>
    <h2 class="title">Sales</h2>
    <p class="hint">Please Enter Amount</p>
    <div class="amount-box">0.01<small>GBP</small></div>
  </section>

  <section class="screen" style="left:490px;top:667px">
    <svg class="back" style="top:64px" width="16" height="10" viewBox="0 0 16 10" fill="none" stroke="#555" stroke-width="1.4"><path d="M15 5H2M6 1L2 5L6 9"/></svg>
    <div class="brand sm" style="top:60px"><span class="dot"></span>Tillora</div>
    <div class="kebab" style="right:20px;top:62px;color:#777"><i></i><i></i><i></i></div>
    <h2 class="title">Sales</h2>
    <div class="amount">0.01 <small>GBP</small></div>
    <div class="pay-option opt-a" role="img" aria-label="Card scheme option"></div>
    <div class="pay-option opt-b" role="img" aria-label="Card scheme option"></div>
    <div class="pay-option opt-c"><svg width="58" height="58" viewBox="0 0 58 58" stroke="#b9c2c9" stroke-width="2"><path d="M29 16V40M17 28H41"/></svg></div>
    <div class="tap">Please Tap<small>Swipe or Insert Card</small></div>
  </section>

  <section class="screen blue" style="left:914px;top:678px">
    <svg class="back" style="top:63px" width="16" height="10" viewBox="0 0 16 10" fill="none" stroke="#fff" stroke-width="1.4"><path d="M15 5H2M6 1L2 5L6 9"/></svg>
    <div class="brand sm" style="top:58px"><span class="dot"></span>Tillora</div>
    <div class="terminal-art" role="img" aria-label="Card terminal illustration"></div>
    <div class="swiping">Swiping Card....</div>
  </section>

</div>
</body>
</html>
```